Business card design needed for Renewable utilities company based in New Zealand.

We supply and install solar panels and all components along with it for a fully customisable PV system that helps customer save money on their energy bills right away and also save the planet!

I have attached logo & website design files to give you a better insight.

Industry/Entity Type

Business

```html
<!DOCTYPE html>
<html lang="en">
<head>
<meta charset="utf-8">
<title>Sun Circuit – Business Card</title>
<link href="https://fonts.googleapis.com/css2?family=Questrial&display=swap" rel="stylesheet">
<style>
  :root {
    --page-bg: #e4e6e9;
    --navy: #151c4f;
    --navy-mid: #1f2f6e;
    --navy-light: #2a4390;
    --sky: #1c9ad6;
    --ink: #1b1e2e;
    --white: #ffffff;
    --map-tone: #eef0f3;
  }
  * { box-sizing: border-box; margin: 0; padding: 0; }
  html, body { width: 1200px; height: 1000px; overflow: hidden; }
  body {
    background: var(--page-bg);
    font-family: "Questrial", "Century Gothic", sans-serif;
    position: relative;
  }

  .card { position: absolute; overflow: hidden; box-shadow: 0 6px 18px rgba(0,0,0,0.18); }

  /* Back side */
  .card-back {
    left: 520px; top: 60px; width: 600px; height: 343px;
    background: linear-gradient(135deg, var(--navy-mid) 0%, var(--navy-light) 100%);
  }
  .card-back .brand {
    position: absolute; right: 48px; top: 170px;
    display: flex; align-items: center; gap: 16px;
    color: var(--white); font-size: 42px; letter-spacing: 1px;
  }
  .brand-dot { width: 56px; height: 56px; border-radius: 50%; background: var(--white); flex: none; }
  .card-back .website {
    position: absolute; right: 70px; top: 244px;
    color: var(--white); font-size: 18px; letter-spacing: 1px;
  }

  /* Front side */
  .card-front {
    left: 90px; top: 500px; width: 720px; height: 410px;
    background: var(--white);
  }
  .world-map {
    position: absolute; left: 90px; top: 24px; width: 560px; height: 300px;
    background: radial-gradient(ellipse at center, var(--map-tone) 0%, rgba(238,240,243,0.4) 70%, rgba(255,255,255,0) 100%);
  }
  .card-front .brand {
    position: absolute; left: 60px; top: 170px;
    display: flex; align-items: center; gap: 14px;
    color: var(--sky); font-size: 40px; letter-spacing: 0.5px;
  }
  .card-front .brand-dot { background: var(--navy-light); width: 60px; height: 60px; }

  .contact { position: absolute; left: 410px; top: 60px; }
  .person-name { color: var(--sky); font-size: 20px; letter-spacing: 0.5px; margin-bottom: 28px; }
  .contact-line { display: flex; align-items: center; gap: 10px; font-size: 15px; color: var(--ink); margin-bottom: 10px; }
  .contact-icon { width: 22px; height: 22px; flex: none; }
  .company { margin-top: 36px; font-size: 15px; color: var(--ink); letter-spacing: 0.3px; }
  .address { color: var(--sky); font-size: 15px; line-height: 1.5; margin-top: 4px; }

  .waves { position: absolute; left: 0; bottom: 0; width: 720px; height: 410px; }
</style>
</head>
<body>

  <section class="card card-back" aria-label="Card back">
    <div class="brand"><span class="brand-dot"></span><span class="brand-name">Sun Circuit</span></div>
    <div class="website">www.suncircuit.co.nz</div>
  </section>

  <section class="card card-front" aria-label="Card front">
    <div class="world-map" role="img" aria-label="Faint dotted world map in light grey"></div>

    <svg class="waves" viewBox="0 0 720 410" aria-hidden="true">
      <path d="M0 410 L0 392 C150 352 300 332 450 320 C320 356 220 388 170 410 Z" fill="var(--sky)"/>
      <path d="M150 410 C300 372 420 300 560 288 C630 283 690 292 720 300 L720 410 Z" fill="var(--navy)"/>
    </svg>

    <div class="brand"><span class="brand-dot"></span><span class="brand-name">Sun Circuit</span></div>

    <div class="contact">
      <p class="person-name">YOUR NAME</p>
      <p class="contact-line">
        <svg class="contact-icon" viewBox="0 0 24 24" aria-hidden="true">
          <circle cx="12" cy="12" r="12" fill="var(--sky)"/>
          <path d="M8.2 6.5c.5-.4 1.1-.3 1.4.2l1.1 1.8c.3.5.2 1-.2 1.4l-.7.6c.6 1.3 1.6 2.4 2.9 3l.6-.7c.4-.4.9-.5 1.4-.2l1.8 1.1c.5.3.6.9.2 1.4l-.8.9c-.6.6-1.5.8-2.3.5-3-1.1-5.3-3.4-6.4-6.4-.3-.8-.1-1.7.5-2.3z" fill="var(--white)"/>
        </svg>
        0800 555 018 240
      </p>
      <p class="contact-line">
        <svg class="contact-icon" viewBox="0 0 24 24" aria-hidden="true">
          <circle cx="12" cy="12" r="12" fill="var(--sky)"/>
          <rect x="6" y="8" width="12" height="8.5" rx="1" fill="var(--white)"/>
          <path d="M6.3 8.4 L12 13 L17.7 8.4" fill="none" stroke="var(--sky)" stroke-width="1.2"/>
        </svg>
        name@suncircuit.co.nz
      </p>
      <p class="company">SUN CIRCUIT</p>
      <p class="address">P.O.Box 482 Road, City. Country<br>NZ 2300</p>
    </div>
  </section>

</body>
</html>
```